KJ Glimmer Cleaning Business Card

We need a business card for our new business, a cleaning company using steam. We already have a logo, and would like a modern-looking card using colors that go well with those in our logo.

```html
<!DOCTYPE html>
<html lang="en">
<head>
<meta charset="utf-8">
<title>KJ Glimmer Cleaning Business Card</title>
<link href="https://fonts.googleapis.com/css2?family=Lato:wght@400;700;900&display=swap" rel="stylesheet">
<style>
  :root {
    --backdrop: #4b4b4b;
    --card: #ffffff;
    --brand-blue: #3b78c4;
    --brand-green: #5aa832;
    --mark-tint: #dfe8f3;
    --ink: #161616;
  }
  * { margin: 0; padding: 0; box-sizing: border-box; }
  html, body { width: 1200px; height: 1000px; overflow: hidden; }
  body { background: var(--backdrop); font-family: "Lato", sans-serif; color: var(--ink); position: relative; }

  .card { position: absolute; background: var(--card); }
  .card-front { left: 166px; top: 123px; width: 611px; height: 358px; }
  .card-back { left: 417px; top: 531px; width: 604px; height: 353px; }

  .brand-mark { position: absolute; border-radius: 50%; background: var(--mark-tint); }
  .card-front .brand-mark { left: 62px; top: 139px; width: 80px; height: 80px; }
  .brand-name {
    position: absolute; left: 170px; top: 136px;
    font-weight: 900; font-size: 44px; line-height: 44px; color: var(--brand-blue);
  }

  .card-back .brand-mark { left: 113px; top: 120px; width: 80px; height: 80px; }
  .brand-name-small {
    position: absolute; left: 40px; top: 214px; width: 226px; text-align: center;
    font-weight: 900; font-size: 20px; line-height: 24px; color: var(--brand-blue);
  }

  .person { position: absolute; left: 336px; top: 47px; }
  .person-name { font-weight: 700; font-size: 21px; line-height: 26px; }
  .person-role { font-size: 16px; color: var(--brand-blue); line-height: 22px; }

  .contacts { position: absolute; left: 336px; top: 121px; list-style: none; }
  .contacts li { display: flex; align-items: center; height: 23.3px; font-size: 14.5px; font-weight: 400; }
  .contacts svg { width: 16px; height: 16px; margin-right: 7px; flex: none; fill: var(--brand-green); }

  .office { position: absolute; left: 338px; top: 236px; }
  .office-name { font-weight: 700; font-size: 17px; line-height: 24px; }
  .office-address { font-size: 14.5px; color: var(--brand-blue); line-height: 23px; }
</style>
</head>
<body>
  <section class="card card-front">
    <div class="brand-mark"></div>
    <div class="brand-name">KJ Glimmer<br>Cleaning</div>
  </section>

  <section class="card card-back">
    <div class="brand-mark"></div>
    <div class="brand-name-small">KJ Glimmer Cleaning</div>

    <div class="person">
      <div class="person-name">Harlan Brooks</div>
      <div class="person-role">President</div>
    </div>

    <ul class="contacts">
      <li><svg viewBox="0 0 16 16"><path d="M3 1.5l2.5 0 1.2 3.3-1.6 1.2a8 8 0 0 0 4.9 4.9l1.2-1.6 3.3 1.2v2.5c0 .8-.7 1.5-1.5 1.5A12.5 12.5 0 0 1 1.5 3c0-.8.7-1.5 1.5-1.5z"/></svg>555 014 2278</li>
      <li><svg viewBox="0 0 16 16"><path d="M4 1h8v4H4zM2 6h12a1 1 0 0 1 1 1v5h-3v3H4v-3H1V7a1 1 0 0 1 1-1zm3 5v3h6v-3z"/></svg>555 014 2279</li>
      <li><svg viewBox="0 0 16 16"><path d="M1 3h14v10H1zm1.5 1.4v.3L8 8.6l5.5-3.9v-.3z"/></svg>harlan.b@kjglimmercleaning.com</li>
      <li><svg viewBox="0 0 16 16"><circle cx="8" cy="8" r="6.5" fill="none" stroke="#5aa832" stroke-width="1.5"/><path d="M1.5 8h13M8 1.5c-3 3.5-3 9.5 0 13M8 1.5c3 3.5 3 9.5 0 13" fill="none" stroke="#5aa832" stroke-width="1.2"/></svg>www.kjglimmercleaning.com</li>
    </ul>

    <div class="office">
      <div class="office-name">KJ Glimmer Cleaning</div>
      <div class="office-address">Suite 118, St. 9, Meadow Lane,<br>NY 10472</div>
    </div>
  </section>
</body>
</html>
```